Halvorn spray foam and Environmental

I have business cards but need new ones. The ones I have are very bland. Here is. Y company website http://www.halvornsprayfoam.ca

Also I can send you copies of the current cards
I would also need my current logo on the new design as well.. Also spray foam and Environmental

Industry/Entity Type

Business

Logo Text

Halvorn.

```html
<!DOCTYPE html>
<html lang="en">
<head>
<meta charset="utf-8">
<title>Halvorn Spray Foam and Environmental — Business Cards</title>
<link rel="stylesheet" href="https://fonts.googleapis.com/css2?family=Montserrat:wght@800&family=Roboto+Condensed:wght@400;700&display=swap">
<style>
  :root{
    --purple:#66337d;
    --grey:#6d6a6b;
    --grey-dark:#5b5859;
    --green:#74bf2c;
    --white:#ffffff;
    --paper:#f4f3f1;
    --mark:#8b8a8c;
    --backdrop:#d9d9d9;
  }
  *{margin:0;padding:0;box-sizing:border-box}
  html,body{width:1200px;height:852px;overflow:hidden;background:var(--backdrop)}
  body{position:relative;font-family:"Roboto Condensed",Arial,sans-serif}
  ul{list-style:none}
  .card{position:absolute;width:540px;height:310px;border-radius:22px;overflow:hidden;box-shadow:0 4px 14px rgba(0,0,0,.18)}

  /* Front */
  .card-front{left:80px;top:110px;background:var(--purple)}
  .front-mark{position:absolute;left:225px;top:62px;width:90px;height:68px;border:3px solid var(--white);border-radius:10px;background:var(--mark)}
  .front-name{position:absolute;left:0;right:0;top:150px;text-align:center;font-family:"Montserrat",Arial,sans-serif;font-weight:800;font-size:66px;color:var(--white);letter-spacing:1px}

  /* Back */
  .card-back{left:580px;top:432px;background:var(--paper)}
  .back-shapes{position:absolute;left:0;top:0}
  .back-brand{position:absolute;left:54px;top:86px;display:flex;align-items:center;gap:14px}
  .back-mark{width:86px;height:60px;border-radius:8px;background:var(--mark);border:2px solid var(--purple)}
  .back-name{font-family:"Montserrat",Arial,sans-serif;font-weight:800;font-size:58px;color:var(--purple);line-height:1}

  .division-title{position:absolute;color:var(--white);font-weight:700;text-transform:uppercase;font-size:20px;line-height:28px}
  .spray-title{left:16px;top:183px}
  .enviro-title{left:306px;top:159px;letter-spacing:.5px}

  .contact{position:absolute;color:var(--white);font-size:12.5px;line-height:14px}
  .contact li{display:flex;align-items:center;gap:6px;height:14px}
  .spray-contact{left:16px;top:215px}
  .enviro-contact{right:16px;top:195px}
  .enviro-contact li{justify-content:flex-end}
  .icon{display:block;width:11px;height:11px;flex:none}

  .services{position:absolute;color:var(--white);font-size:10px;line-height:11px;display:grid;grid-template-rows:repeat(4,11px);grid-auto-flow:column;column-gap:10px;white-space:nowrap}
  .spray-services{left:16px;top:260px}
  .enviro-services{right:16px;top:241px;text-align:right}
  .spray-services li::before{content:"» "}
  .enviro-services li::after{content:" «"}
</style>
</head>
<body>

<section class="card card-front" aria-label="Business card front">
  <div class="front-mark"></div>
  <div class="front-name">HALVORN</div>
</section>

<section class="card card-back" aria-label="Business card back">
  <svg class="back-shapes" width="540" height="310" viewBox="0 0 540 310" aria-hidden="true">
    <polygon points="0,176 220,176 245,150 290,150 290,310 0,310" fill="var(--purple)"/>
    <rect x="0" y="183" width="290" height="28" fill="var(--grey-dark)"/>
    <polygon points="245,150 540,150 540,310 290,310 290,158 262,150" fill="var(--grey)"/>
    <rect x="290" y="159" width="250" height="28" fill="var(--green)"/>
  </svg>

  <div class="back-brand">
    <div class="back-mark"></div>
    <div class="back-name">HALVORN</div>
  </div>

  <div class="division-title spray-title">Spray Foam</div>
  <div class="division-title enviro-title">Environmental</div>

  <ul class="contact spray-contact">
    <li><svg class="icon" viewBox="0 0 12 12"><circle cx="6" cy="6" r="5" fill="none" stroke="#fff"/><path d="M4 3.5l1 1.5-.6.6a4 4 0 0 0 2 2l.6-.6 1.5 1-.8.9C5.5 8.5 3.5 6.5 3.2 4.3z" fill="#fff"/></svg>604-555-0147</li>
    <li><svg class="icon" viewBox="0 0 12 12"><rect x="1" y="2.5" width="10" height="7" fill="none" stroke="#fff"/><path d="M1 2.5l5 4 5-4" fill="none" stroke="#fff"/></svg>halvornfoam@mailbox.ca</li>
    <li><svg class="icon" viewBox="0 0 12 12"><circle cx="6" cy="6" r="5" fill="none" stroke="#fff"/><path d="M1 6h10M6 1c-3 3-3 7 0 10M6 1c3 3 3 7 0 10" fill="none" stroke="#fff" stroke-width=".8"/></svg>www.halvornsprayfoam.ca</li>
  </ul>
  <ul class="services spray-services">
    <li>Roofing Foam</li><li>2 Pound / Half Pound</li><li>Sound Proofing</li><li>Batt Insulation</li><li>Slab Jacking</li><li>Attic Blow in</li>
  </ul>

  <ul class="contact enviro-contact">
    <li>604-555-0182<svg class="icon" viewBox="0 0 12 12"><circle cx="6" cy="6" r="5" fill="none" stroke="#fff"/><path d="M4 3.5l1 1.5-.6.6a4 4 0 0 0 2 2l.6-.6 1.5 1-.8.9C5.5 8.5 3.5 6.5 3.2 4.3z" fill="#fff"/></svg></li>
    <li>halvornenviro1@mailbox.ca<svg class="icon" viewBox="0 0 12 12"><rect x="1" y="2.5" width="10" height="7" fill="none" stroke="#fff"/><path d="M1 2.5l5 4 5-4" fill="none" stroke="#fff"/></svg></li>
    <li>www.halvornenvironmental.ca<svg class="icon" viewBox="0 0 12 12"><circle cx="6" cy="6" r="5" fill="none" stroke="#fff"/><path d="M1 6h10M6 1c-3 3-3 7 0 10M6 1c3 3 3 7 0 10" fill="none" stroke="#fff" stroke-width=".8"/></svg></li>
  </ul>
  <ul class="services enviro-services">
    <li></li><li>Air Monitoring</li><li></li><li>Lead Testing</li>
    <li>Asbestos Testing</li><li>Asbestos Removal</li><li>Building Demolition</li><li>Mould Removal</li>
  </ul>
</section>

</body>
</html>
```